ORVI LTH website - sleek, sophisticated, uplifting

ORVI Institute for Restorative Care is a cutting-edge medical clinic aimed at providing treatment for various chronic conditions and help people stave off the declines usually associated with aging. We utilize the latest technology in regenerative medicine to help people with autoimmune conditions, musculoskeletal problems and chronic pain, neurodegenerative conditions, male enhancement, facial rejuvenation and hair restoration, etc. We provide personalized medicine, through highly compassionate and competent doctors and staff.

please look at my current website which is not focused on regenerative medicine, but some contents can stay, as far as the philosophy of the treatment: www.pbmosaicwellness-example.com. But the reason I am changing the name of the clinic is because the focus of the medical practice is shifted entirely to "regenerative medicine" - using the body's own healing mechanism such as stem cells and growth factors...

Please DO NOT recycle old graphics and pictures. I want this site to be brand new, fresh and original.

Would like the website to be more sophisticated and nicer-looking than this website: www.duskmere-example.com

Target Market(s)

People who care a great deal about their health (above age 35), wants to prevent declines in their looks and health as they are getting older. Generally high income sector of the society that can afford self-pay (no insurance accepted) expensive stem cell treatment ranging from $4000 to $20,000.

Industry/Entity Type

Healthcare

Coding

Coded - Design and coding required

Number of Pages Required

5+ page

Font styles to use
Sans Serif
Other font styles liked:
• Al Bayan, Avenir, Didot, Open Sans or Tsukushi A Round Gothic for central text, but may use Chalkboard for titles, or others as seen fit

Colors

Designer to choose colors to be used in the design.

Requirements
Must have
• Ultra modern look, very clean & sleek images and layout, portraying a sense of sophistication and confidence. Works beautifully well with existing logo. Give a sense that the clinic employs cutting-edge science, and provide highly competent & compassionate services.
• More sophisticated and nicer-looking than this website: www.duskmere-example.com
Nice to have
• many pages and links to science articles
Should not have
• fonts too playful or hard to read.

```html
<!DOCTYPE html>
<html lang="en">
<head>
<meta charset="utf-8">
<title>ORVI Institute for Restorative Care – Contact</title>
<link href="https://fonts.googleapis.com/css2?family=Jost:wght@400;500;600;700;800&family=Open+Sans:wght@400;600&display=swap" rel="stylesheet">
<style>
  :root {
    --gold: #c8922f;
    --ink: #1f1c1c;
    --text: #3a3a3a;
    --line: #9a9a9a;
    --footer-bg: #f4f4f4;
    --white: #ffffff;
  }
  * { box-sizing: border-box; margin: 0; padding: 0; }
  html, body { width: 1133px; height: 1200px; overflow: hidden; background: var(--white); }
  body { position: relative; font-family: "Open Sans", Arial, sans-serif; color: var(--text); }

  .brand { position: absolute; top: 14px; left: 0; width: 1133px; text-align: center; }
  .brand-dot { width: 56px; height: 56px; border-radius: 50%; background: var(--gold); margin: 0 auto 12px; }
  .brand-name { font-family: "Jost", sans-serif; font-weight: 500; font-size: 46px; line-height: 42px; letter-spacing: 1px; color: var(--ink); }
  .brand-sub { font-family: "Jost", sans-serif; font-weight: 500; font-size: 9.5px; color: var(--ink); margin-top: 3px; }

  .main-nav { position: absolute; top: 176px; left: 0; width: 1133px; display: flex; justify-content: center; gap: 64px; }
  .main-nav a { font-family: "Jost", sans-serif; font-size: 16.5px; color: var(--ink); text-decoration: none; padding-bottom: 6px; }
  .main-nav a.is-active { color: var(--gold); border-bottom: 2px solid var(--gold); }

  .page-hero { position: absolute; top: 221px; left: 0; width: 1133px; height: 288px;
    background: radial-gradient(ellipse at 25% 45%, #4a4a4a 0%, #7a7a7a 35%, transparent 60%),
                radial-gradient(ellipse at 72% 55%, #555 0%, #8a8a8a 25%, transparent 45%),
                linear-gradient(90deg, #a9a9a9, #cfcfcf 50%, #bdbdbd);
    display: flex; align-items: center; justify-content: center; }
  .page-hero h1 { font-family: "Jost", sans-serif; font-weight: 600; font-size: 52px; color: var(--white); letter-spacing: 1px; margin-top: -18px; }

  .section-title { position: absolute; top: 588px; left: 0; width: 1133px; text-align: center;
    font-family: "Jost", sans-serif; font-weight: 800; font-size: 32px; color: var(--ink); letter-spacing: 0.5px; }

  .contact-info { position: absolute; top: 698px; left: 94px; width: 360px; font-size: 17.5px; line-height: 25px; }
  .contact-info p { margin-bottom: 15px; }
  .contact-info strong { font-weight: 600; color: #333; }
  .contact-info svg { vertical-align: -2px; margin-right: 6px; }
  .social { display: flex; gap: 7px; margin-top: 18px; }
  .social span { width: 33px; height: 33px; border: 2px solid var(--gold); border-radius: 50%; }

  .contact-form { position: absolute; top: 699px; left: 518px; width: 521px; }
  .field { display: block; width: 100%; height: 35px; border: 1px solid var(--line); margin-bottom: 22px;
    font-family: "Open Sans", sans-serif; font-size: 15px; color: #444; padding: 6px 14px; }
  .field-message { height: 87px; margin-bottom: 34px; }
  .submit { display: inline-block; width: 116px; height: 36px; background: var(--gold); color: var(--white);
    font-family: "Jost", sans-serif; font-weight: 600; font-size: 12.5px; text-align: center; line-height: 36px; }

  .site-footer { position: absolute; top: 1125px; left: 0; width: 1133px; height: 75px; background: var(--footer-bg);
    text-align: center; font-size: 12.5px; line-height: 75px; color: #444; }
</style>
</head>
<body>
  <header class="brand">
    <div class="brand-dot"></div>
    <div class="brand-name">ORVI</div>
    <div class="brand-sub">Institute for Restorative Care</div>
  </header>

  <nav class="main-nav">
    <a href="#">HOME</a>
    <a href="#">ABOUT</a>
    <a href="#">SERVICES</a>
    <a href="#">SCIENCE</a>
    <a href="#" class="is-active">CONTACT</a>
  </nav>

  <section class="page-hero" role="img" aria-label="Soft-focus black and white photo of a figure behind a grass plume">
    <h1>CONTACT US</h1>
  </section>

  <h2 class="section-title">REACH OUT TO US</h2>

  <div class="contact-info">
    <p><svg width="11" height="15" viewBox="0 0 11 15"><path d="M5.5 0C2.5 0 0 2.4 0 5.4 0 9 5.5 15 5.5 15S11 9 11 5.4C11 2.4 8.5 0 5.5 0z" fill="#c8922f"/><circle cx="5.5" cy="5.3" r="2" fill="#fff"/></svg><strong>Address:</strong> 2740 Larkfield Road Suite 210 Brenmoor CA 90412</p>
    <p><svg width="15" height="15" viewBox="0 0 24 24"><path d="M6.6 10.8c1.4 2.8 3.8 5.1 6.6 6.6l2.2-2.2c.3-.3.7-.4 1-.2 1.1.4 2.3.6 3.6.6.6 0 1 .4 1 1V20c0 .6-.4 1-1 1C10.6 21 3 13.4 3 4c0-.6.4-1 1-1h3.5c.6 0 1 .4 1 1 0 1.3.2 2.5.6 3.6.1.3 0 .7-.2 1z" fill="#c8922f"/></svg><strong>Call Us:</strong> +1 555 014 2268</p>
    <p><svg width="17" height="14" viewBox="0 0 17 14"><rect x="1" y="1" width="15" height="12" rx="1" fill="none" stroke="#c8922f" stroke-width="1.6"/><path d="M1.5 2l7 6 7-6" fill="none" stroke="#c8922f" stroke-width="1.6"/></svg><strong>Email:</strong> hello@orvi-example.com</p>
    <div class="social"><span></span><span></span><span></span></div>
  </div>

  <form class="contact-form">
    <div class="field">Name</div>
    <div class="field">Email address</div>
    <div class="field">Subject</div>
    <div class="field field-message">Message</div>
    <span class="submit">SUBMIT NOW</span>
  </form>

  <footer class="site-footer">© 2018 ORVI Institute for Restorative Care.&nbsp; All right reserved.&nbsp; Term of Use</footer>
</body>
</html>
```